I need a label design to go on our jars of honey. Our company is called Quillbrook Honey Co. The type of honey is called Marram Glade Honey. The jars are 1kg. Attached is the label size. Left hand side needs to have nutritional info... as attached. Middle section is our company name, honey type, 1kg & Whangamata, NZ. Right hand side needs to have info as per photo (raw honey etc). I would like to upload more pictures... but I’m unsure how to do this? Thanks, Noreen

Target Market(s)

Honey consumers... families

Industry/Entity Type

Food Production

Colors

Designer to choose colors to be used in the design.

Requirements
Must have
• Nutritional info as per upload
• Type of honey & company name as per upload
• 1kg
• Address
Nice to have
• Similar fonts to upload.
• Possibly background image... floral or beach... very faint though.

```html
<!DOCTYPE html>
<html lang="en">
<head>
<meta charset="utf-8">
<title>Quillbrook Honey Co. – Marram Glade Honey label</title>
<link rel="stylesheet" href="https://fonts.googleapis.com/css2?family=Josefin+Sans:wght@300&family=Sacramento&family=Shadows+Into+Light+Two&family=PT+Serif&display=swap">
<style>
  :root {
    --ink: #111111;
    --paper: #ffffff;
    --wash: rgba(255, 255, 255, 0.72);
    --panel-wash: rgba(255, 255, 255, 0.9);
    --gold: #e7b62a;
    --meadow-green: #9fb08a;
    --meadow-violet: #8f86b4;
    --meadow-red: #d98a74;
  }
  * { box-sizing: border-box; margin: 0; padding: 0; }
  html, body { width: 1200px; height: 480px; overflow: hidden; background: var(--paper); }

  .label {
    position: relative;
    width: 1200px;
    height: 480px;
    overflow: hidden;
    color: var(--ink);
  }

  .label__backdrop {
    position: absolute;
    inset: 0;
    background:
      radial-gradient(circle at 22% 35%, var(--meadow-red) 0, transparent 18%),
      radial-gradient(circle at 40% 70%, var(--meadow-red) 0, transparent 14%),
      radial-gradient(circle at 62% 45%, var(--meadow-red) 0, transparent 16%),
      radial-gradient(circle at 80% 30%, var(--meadow-violet) 0, transparent 25%),
      radial-gradient(circle at 10% 80%, var(--meadow-violet) 0, transparent 22%),
      radial-gradient(circle at 50% 20%, var(--meadow-violet) 0, transparent 20%),
      linear-gradient(160deg, var(--meadow-green), #b7b59a 50%, var(--meadow-violet));
  }
  .label__backdrop::after {
    content: "";
    position: absolute;
    inset: 0;
    background: var(--wash);
  }

  /* Left: nutrition */
  .nutrition-side {
    position: absolute;
    left: 36px;
    top: 20px;
    width: 204px;
    font-family: "PT Serif", serif;
    font-size: 12px;
    line-height: 1.18;
    text-align: center;
    letter-spacing: -0.2px;
  }
  .nutrition-side__claim { margin-left: -4px; }
  .nutrition-panel {
    margin-top: 6px;
    border: 1.5px solid var(--gold);
    background: var(--panel-wash);
    text-align: left;
  }
  .nutrition-panel__head {
    padding: 5px 18px 4px;
    border-bottom: 1.5px solid var(--gold);
  }
  .nutrition-panel__title { text-align: center; font-weight: 700; font-size: 12.5px; }
  .nutrition-table { width: 100%; border-collapse: collapse; font-size: 12px; }
  .nutrition-table th {
    font-weight: 400;
    text-align: left;
    vertical-align: top;
    padding: 3px 0 8px;
    line-height: 1.05;
  }
  .nutrition-table td { padding: 1px 0 4px; white-space: nowrap; }
  .nutrition-table td:first-child { padding-left: 4px; width: 70px; }
  .nutrition-table td:nth-child(2) { width: 78px; }
  .nutrition-table .is-sub { padding-left: 26px !important; }
  .nutrition-side__care { margin-top: 7px; line-height: 1.2; }
  .batch-panel {
    margin-top: 9px;
    border: 1.5px solid var(--gold);
    background: var(--panel-wash);
    text-align: left;
    padding: 4px 0 4px 12px;
    line-height: 1.55;
  }
  .batch-panel span { display: inline-block; width: 58px; }

  /* Centre: brand */
  .brand {
    position: absolute;
    left: 380px;
    width: 440px;
    top: 30px;
    text-align: center;
  }
  .brand__name {
    font-family: "Josefin Sans", sans-serif;
    font-weight: 300;
    font-size: 40px;
    line-height: 1.3;
    letter-spacing: 9px;
    transform: scaleX(0.82);
  }
  .brand__product {
    font-family: "Sacramento", cursive;
    font-weight: 400;
    font-size: 96px;
    line-height: 0.98;
    margin-top: 4px;
  }
  .brand__weight {
    font-family: "Sacramento", cursive;
    font-size: 38px;
    margin-top: 8px;
  }
  .brand__weight small { font-family: "Josefin Sans", sans-serif; font-size: 18px; font-weight: 300; }
  .brand__place {
    font-family: "Josefin Sans", sans-serif;
    font-weight: 300;
    font-size: 22px;
    letter-spacing: 5px;
    margin-top: 8px;
  }

  /* Right: story */
  .story {
    position: absolute;
    left: 880px;
    width: 300px;
    top: 30px;
    text-align: center;
    font-family: "Shadows Into Light Two", cursive;
  }
  .story__origin { font-size: 20px; line-height: 1.25; letter-spacing: 1px; }
  .story__raw { font-size: 13.5px; line-height: 1.55; margin-top: 22px; }
  .story__signoff { font-size: 20px; line-height: 1.2; margin-top: 28px; letter-spacing: 1.5px; }
  .story__thanks { font-size: 14px; line-height: 1.5; margin-top: 24px; }
  .story__web { font-size: 16px; letter-spacing: 3px; margin-top: 30px; }
  .story__address { font-size: 15px; line-height: 1.5; margin-top: 24px; }
</style>
</head>
<body>
<main class="label">
  <div class="label__backdrop" role="img" aria-label="Very faint photograph of a flowering garden with purple and red blooms"></div>

  <section class="nutrition-side">
    <p class="nutrition-side__claim">100% New Zealand Honey<br>No added ingredients</p>
    <div class="nutrition-panel">
      <div class="nutrition-panel__head">
        <p class="nutrition-panel__title">NUTRITIONAL INFORMATION</p>
        <p>Serving per package: 100</p>
        <p>Serving size: 10g</p>
      </div>
      <table class="nutrition-table">
        <tr><td></td><th>Average<br>Quanity<br>per Serving</th><th>Average<br>Quanity<br>per 100g</th></tr>
        <tr><td>Energy</td><td>134kj</td><td>1340kj</td></tr>
        <tr><td>Protein</td><td>0.04g</td><td>0.4g</td></tr>
        <tr><td>Fat total</td><td>0g</td><td>0g</td></tr>
        <tr><td class="is-sub">saturated</td><td>0g</td><td>0g</td></tr>
        <tr><td>Carbohydrate</td><td>7.9g</td><td>79.6g</td></tr>
        <tr><td class="is-sub">sugars</td><td>7.8g</td><td>78.1g</td></tr>
        <tr><td>Sodium</td><td>1.2mg</td><td>12mg</td></tr>
      </table>
    </div>
    <p class="nutrition-side__care">Store upright in a cool, dry place.<br>No refrigeration needed.<br>Not recommended for infants below<br>the age of 12 months.</p>
    <div class="batch-panel">
      <p><span>Best before</span>:</p>
      <p><span>RMP</span>:</p>
      <p><span>Batch No</span>:</p>
    </div>
  </section>

  <section class="brand">
    <h1 class="brand__name">QUILLBROOK<br>HONEY CO.</h1>
    <h2 class="brand__product">Marram<br>Glade Honey</h2>
    <p class="brand__weight">1<small>KG</small></p>
    <p class="brand__place">WHANGAMATA NZ</p>
  </section>

  <section class="story">
    <p class="story__origin">Sourced from the beautiful<br>Coromandel Peninsula</p>
    <p class="story__raw">Our honey comes to you raw &amp; unpasteurised,<br>ensuring it retains all the natural goodness!</p>
    <p class="story__signoff">Arohanui,<br>Rowan, Noreen &amp; Boys</p>
    <p class="story__thanks">"Quillbrook" – all thanks to God<br>for His incredible creation!</p>
    <p class="story__web">www.quillbrookhoney.co.nz</p>
    <p class="story__address">42 Tidewater Rd<br>Whangamata, New Zealand</p>
  </section>
</main>
</body>
</html>
```